Larkfield Holdings Template for Power Point

Need these all files converted and reformatted o power points to copy look and feel of website . http://larkfieldholdings.example

Target Market(s)

Real Estate

Requirements
Must have
• Congruent with LarkfieldHoldings.example

```html
<!DOCTYPE html>
<html lang="en">
<head>
<meta charset="utf-8">
<title>Property Information – 4631 Harlow Avenue</title>
<link href="https://fonts.googleapis.com/css2?family=Montserrat:wght@400;600;700;800&family=Open+Sans:wght@400;600;700&display=swap" rel="stylesheet">
<style>
:root{
  --gold:#f4b11c;
  --gold-deep:#e39a0e;
  --ink:#2d2d2d;
  --muted:#555;
  --paper:#ffffff;
  --band:#f1f1f1;
  --navy:#1f3a5c;
}
*{box-sizing:border-box;margin:0;padding:0}
html,body{width:1200px;height:2512px;overflow:hidden;background:var(--paper)}
body{font-family:"Open Sans",Arial,sans-serif;color:var(--ink);position:relative}
.abs{position:absolute}
.photo{position:absolute;border-radius:2px}
.ph-house{background:linear-gradient(180deg,#8ea4b8 0%,#6f7d6a 55%,#4e5b3c 100%)}
.ph-room{background:linear-gradient(160deg,#cdbfa8 0%,#a79276 100%)}
.ph-bath{background:linear-gradient(160deg,#e8e4dc 0%,#bdb6aa 100%)}
.ph-kitchen{background:linear-gradient(160deg,#b59a74 0%,#7b6146 100%)}
.ph-dark{background:linear-gradient(160deg,#6d625a 0%,#3f3833 100%)}

/* hero */
.hero{left:0;top:0;width:1200px;height:500px;background:linear-gradient(180deg,#5a6f86 0%,#6d6256 55%,#3d4a2c 100%)}
.hero-shade{left:0;top:0;width:1200px;height:500px;background:rgba(0,0,0,.38)}
.hero-icon{left:550px;top:225px}
.hero-kicker{left:0;top:368px;width:1200px;text-align:center;font-family:"Montserrat",sans-serif;font-weight:700;font-size:26px;letter-spacing:1px;color:#fff}
.hero-title{left:0;top:408px;width:1200px;text-align:center;font-family:"Montserrat",sans-serif;font-weight:800;font-size:46px;color:var(--gold)}

/* headings */
.sec-head{font-family:"Montserrat",sans-serif;font-weight:800;font-size:19px;color:var(--ink);display:flex;align-items:center;gap:12px;text-transform:uppercase;white-space:nowrap}
.sec-head::before{content:"";width:14px;height:30px;background:var(--gold);flex:none}
.list{list-style:none;font-size:13px;line-height:21px;color:var(--muted)}
.list li::before{content:"• ";color:var(--gold-deep);font-weight:700}
.sub{font-family:"Montserrat",sans-serif;font-weight:700;font-size:15px;color:var(--gold-deep);margin:10px 0 4px}

/* property facts */
.price{left:40px;top:542px;width:220px;font-family:"Montserrat",sans-serif;font-weight:700;font-size:14px;color:var(--gold-deep);white-space:nowrap}
.facts{left:40px;top:575px;width:220px;font-size:12px;line-height:19px;color:var(--muted)}
.facts b{color:var(--ink)}

/* kitchen band */
.band{left:0;top:935px;width:1200px;height:650px;background:var(--band)}
.tile-label{position:absolute;width:174px;text-align:center;font-family:"Montserrat",sans-serif;font-weight:700;font-size:12px;letter-spacing:1px;color:var(--ink)}
.note-box{left:312px;top:1235px;width:250px;height:330px;background:var(--gold);padding:12px 16px;font-size:12px;line-height:18px;color:var(--ink)}
.note-box h4{font-family:"Montserrat",sans-serif;font-size:14px;margin:6px 0 2px}

/* bedrooms */
.bed-head{left:40px;top:1620px;width:520px;font-family:"Montserrat",sans-serif;font-weight:700;font-size:22px;color:var(--ink);text-align:center;white-space:nowrap}
.bed-head span{display:inline-block;border-bottom:5px solid var(--gold);padding-bottom:6px}
.room-name{font-family:"Montserrat",sans-serif;font-weight:700;font-size:18px;color:var(--gold-deep);margin:18px 0 4px}

/* closing */
.brand{left:780px;top:2300px;display:flex;align-items:center;gap:12px;font-family:"Montserrat",sans-serif;font-weight:800;font-size:30px;color:var(--navy)}
.brand i{width:26px;height:26px;background:var(--navy);display:block}
.thanks{left:600px;top:2390px;width:600px;text-align:center;font-family:"Montserrat",sans-serif;font-weight:800;font-size:64px;color:var(--gold)}
</style>
</head>
<body>

<!-- Hero -->
<div class="abs hero" role="img" aria-label="Front exterior of the brick house with lawn and trees"></div>
<div class="abs hero-shade"></div>
<svg class="abs hero-icon" width="100" height="100" viewBox="0 0 100 100" aria-hidden="true">
  <path d="M50 8 L94 48 H80 V92 H20 V48 H6 Z" fill="#fff"/>
  <rect x="68" y="14" width="10" height="22" fill="#fff"/>
  <rect x="41" y="62" width="18" height="30" fill="#6b6b6b"/>
</svg>
<div class="abs hero-kicker">PROPERTY INFORMATION FOR</div>
<div class="abs hero-title">4631 Harlow Avenue, Memphis, TN 38128</div>

<!-- Property facts & exterior -->
<div class="abs price">Purchase Price $134,900.00</div>
<div class="abs facts">
  <b>Number of Bedrooms:</b> 3<br>
  <b>Number of Bathrooms:</b> 1.5<br>
  <b>Sq. Footage:</b> 1,325<br><br>
  <b>Estimated Rental Income:</b><br>$975 per month<br><br>
  <b>Estimated Rehab &amp; Holding Cost:</b><br>$31,400<br><br>
  <b>Estimated Return:</b><br>Gross Yield 8.7%<br>Net Yield 6.1%<br>Cash flow $3,510 per year<br>Appreciation 3% annually
</div>
<div class="photo ph-house" style="left:270px;top:545px;width:140px;height:100px" role="img" aria-label="House front before renovation"></div>
<div class="photo ph-house" style="left:420px;top:545px;width:140px;height:100px" role="img" aria-label="House front after renovation"></div>
<div class="photo ph-house" style="left:270px;top:655px;width:140px;height:100px" role="img" aria-label="Side of the house"></div>
<div class="photo ph-house" style="left:420px;top:655px;width:140px;height:100px" role="img" aria-label="Backyard view"></div>
<div class="photo ph-house" style="left:270px;top:765px;width:290px;height:130px" role="img" aria-label="Street view of the finished home"></div>

<div class="abs sec-head" style="left:600px;top:535px">Work performed on the home's exterior</div>
<ul class="abs list" style="left:610px;top:585px;width:270px">
  <li>Pressure wash</li><li>Trim shrubs and tree limbs</li><li>Install new gutters</li><li>Paint trim</li><li>Paint soffits</li><li>Paint shutters</li><li>Paint front and back doors</li><li>Patch roof leaks</li><li>Replace missing shingles</li><li>Seal driveway cracks</li><li>Install new mailbox</li><li>Clean gutters and downspouts</li><li>Replace rotted fascia boards</li><li>Repair porch railing</li><li>New light fixtures outside</li><li>Install new house numbers</li>
</ul>
<ul class="abs list" style="left:890px;top:585px;width:270px">
  <li>New deadbolt locks</li><li>New storm door</li><li>New fence panels as needed</li><li>New fence gate latch</li><li>Replace window screens</li><li>Caulk all windows</li><li>Repair foundation vents</li><li>Regrade soil away from walls</li><li>New crawlspace cover</li><li>Reseal back patio slab</li><li>Repair and paint exterior siding</li><li>Replace AC condenser pad</li><li>Haul away debris from yard</li><li>Fresh mulch in beds</li>
</ul>

<!-- Kitchen band -->
<div class="abs band"></div>
<div class="abs sec-head" style="left:40px;top:965px">Work performed on the home's kitchen</div>
<ul class="abs list" style="left:50px;top:1012px;width:510px">
  <li>Install new countertops and backsplash</li><li>Install new sink and faucet</li><li>Install new cabinet hardware</li><li>Install new range hood as needed</li><li>Install new dishwasher</li><li>Paint cabinets inside and out</li><li>Install new light fixtures</li><li>Replace flooring with vinyl plank</li><li>Patch and paint walls and ceiling</li><li>Install new outlet covers and switches</li>
</ul>

<div class="photo ph-bath" style="left:40px;top:1235px;width:130px;height:160px" role="img" aria-label="Bathroom vanity"></div>
<div class="photo ph-bath" style="left:178px;top:1235px;width:126px;height:160px" role="img" aria-label="Bathroom tub"></div>
<div class="photo ph-bath" style="left:40px;top:1405px;width:130px;height:160px" role="img" aria-label="Half bath toilet"></div>
<div class="photo ph-bath" style="left:178px;top:1405px;width:126px;height:160px" role="img" aria-label="Half bath sink"></div>
<div class="abs note-box">
  <h4>Hallway Bathroom</h4>
  Install new vanity and faucet<br>New toilet and seat<br>Reglaze tub and tile surround<br>New shower rod and head<br>Replace floor tile<br>Paint walls and ceiling
  <h4>Master Bathroom</h4>
  Install new vanity and mirror<br>New toilet and seat<br>Replace exhaust fan<br>New light fixture<br>Paint walls and ceiling<br>Caulk tub and fixtures
</div>

<!-- before/after grid -->
<div class="photo ph-kitchen" style="left:600px;top:960px;width:174px;height:120px" role="img" aria-label="Kitchen before"></div>
<div class="photo ph-kitchen" style="left:793px;top:960px;width:174px;height:120px" role="img" aria-label="Kitchen before"></div>
<div class="photo ph-kitchen" style="left:986px;top:960px;width:174px;height:120px" role="img" aria-label="Kitchen before"></div>
<div class="tile-label" style="left:600px;top:1084px">BEFORE</div>
<div class="tile-label" style="left:793px;top:1084px">BEFORE</div>
<div class="tile-label" style="left:986px;top:1084px">BEFORE</div>

<div class="photo ph-room" style="left:600px;top:1110px;width:174px;height:120px" role="img" aria-label="Kitchen after"></div>
<div class="photo ph-room" style="left:793px;top:1110px;width:174px;height:120px" role="img" aria-label="Kitchen after"></div>
<div class="photo ph-room" style="left:986px;top:1110px;width:174px;height:120px" role="img" aria-label="Kitchen after"></div>
<div class="tile-label" style="left:600px;top:1234px">AFTER</div>
<div class="tile-label" style="left:793px;top:1234px">AFTER</div>
<div class="tile-label" style="left:986px;top:1234px">AFTER</div>

<div class="photo ph-dark" style="left:600px;top:1260px;width:174px;height:120px" role="img" aria-label="Living room before"></div>
<div class="photo ph-dark" style="left:793px;top:1260px;width:174px;height:120px" role="img" aria-label="Dining area before"></div>
<div class="photo ph-dark" style="left:986px;top:1260px;width:174px;height:120px" role="img" aria-label="Hallway before"></div>
<div class="tile-label" style="left:600px;top:1384px">BEFORE</div>
<div class="tile-label" style="left:793px;top:1384px">BEFORE</div>
<div class="tile-label" style="left:986px;top:1384px">BEFORE</div>

<div class="photo ph-room" style="left:600px;top:1410px;width:174px;height:120px" role="img" aria-label="Living room after"></div>
<div class="photo ph-room" style="left:793px;top:1410px;width:174px;height:120px" role="img" aria-label="Dining area after"></div>
<div class="photo ph-room" style="left:986px;top:1410px;width:174px;height:120px" role="img" aria-label="Hallway after"></div>
<div class="tile-label" style="left:600px;top:1534px">AFTER</div>
<div class="tile-label" style="left:793px;top:1534px">AFTER</div>
<div class="tile-label" style="left:986px;top:1534px">AFTER</div>

<!-- Bedrooms -->
<div class="abs bed-head"><span>Work Performed On The Home's Bedrooms</span></div>
<div class="abs" style="left:50px;top:1680px;width:300px">
  <div class="room-name">Bedroom 1:</div>
  <ul class="list"><li>Install new support bracket for closet bar</li><li>Install new ceiling fan with light</li></ul>
  <div class="room-name">Bedroom 2:</div>
  <ul class="list"><li>Install new support bracket for closet bar</li><li>Replace carpet with vinyl plank</li></ul>
  <div class="room-name">Master Bedroom:</div>
  <ul class="list"><li>Install new support bracket for closet bar</li><li>New ceiling fan with light</li></ul>
</div>
<div class="photo ph-room" style="left:370px;top:1690px;width:190px;height:120px" role="img" aria-label="Bedroom with ceiling fan"></div>
<div class="photo ph-room" style="left:370px;top:1820px;width:190px;height:120px" role="img" aria-label="Second bedroom"></div>
<div class="photo ph-room" style="left:370px;top:1950px;width:190px;height:120px" role="img" aria-label="Master bedroom"></div>

<div class="abs sec-head" style="left:600px;top:1622px">Additional work performed:</div>
<div class="abs" style="left:610px;top:1665px;width:270px">
  <div class="sub">Electrical:</div>
  <ul class="list"><li>New GFCI outlets</li><li>New smoke detectors</li><li>Replace broken switches</li></ul>
  <div class="sub">Plumbing:</div>
  <ul class="list"><li>New water heater</li><li>Repair leaks under sinks</li><li>New shutoff valves</li></ul>
  <div class="sub">HVAC:</div>
  <ul class="list"><li>Service furnace and AC</li><li>New thermostat</li><li>Replace air filters</li></ul>
  <div class="sub">Flooring:</div>
  <ul class="list"><li>Install vinyl plank flooring</li><li>New baseboards as needed</li></ul>
</div>
<div class="abs" style="left:890px;top:1665px;width:270px">
  <div class="sub">Living Room:</div>
  <ul class="list"><li>Patch and paint walls</li><li>New ceiling fan</li><li>New blinds</li></ul>
  <div class="sub">Laundry Room:</div>
  <ul class="list"><li>New dryer vent</li><li>Paint walls</li></ul>
  <div class="sub">Interior:</div>
  <ul class="list"><li>Paint entire interior</li><li>New interior door knobs</li><li>New closet doors</li><li>Replace light fixtures</li><li>Clean entire house</li><li>Pest inspection and treatment</li></ul>
</div>

<!-- Closing -->
<div class="photo ph-room" style="left:40px;top:2200px;width:165px;height:130px" role="img" aria-label="Finished kitchen"></div>
<div class="photo ph-bath" style="left:217px;top:2200px;width:165px;height:130px" role="img" aria-label="Finished bathroom"></div>
<div class="photo ph-room" style="left:394px;top:2200px;width:166px;height:130px" role="img" aria-label="Finished bedroom"></div>
<div class="photo ph-dark" style="left:40px;top:2345px;width:255px;height:130px" role="img" aria-label="Living room"></div>
<div class="photo ph-house" style="left:305px;top:2345px;width:255px;height:130px" role="img" aria-label="Finished house exterior"></div>
<div class="abs brand"><i></i>Larkfield Holdings</div>
<div class="abs thanks">THANK YOU</div>

</body>
</html>
```